SipLoop Business Cards

Hi designers!

Here's some background on our start-up and this project:

SipLoop is a website that will allow users to order alcohol from nearby liquor stores and have it delivered to their homes in minutes. We are really excited to work on creating the best online, alcohol purchasing experience for the users.

So why SipLoop? We like to think of ourselves as that great friend who will get alcohol for you because he happens to have a car. We help you drink in with your friends, family, or guests. Our site will target students and young professionals (of drinking age) who are comfortable buying things online or through apps. We don't see this service as a luxury, VIP, or niche service in the least; instead, we think of us as a relaxed, service-driven start-up that believes in simple design and transparent .

Now, we want a business card that incorporates our newly acquired logo design and some complimenting colors and fonts. Feel free to do it single or double sided, although I'm a sucker for double...

If you happen to have any questions, want to throw some ideas around, or just want some feedback- email me at marco@siploop.example.

Marco Tessin
Founder

Industry/Entity Type

Business

Requirements
Must have
• Name, Position, Email, Cell-phone

No address, no fax, no land-line.

```html
<!DOCTYPE html>
<html lang="en">
<head>
<meta charset="utf-8">
<title>SipLoop Business Cards</title>
<link href="https://fonts.googleapis.com/css2?family=Poppins:wght@400;600;800&display=swap" rel="stylesheet">
<style>
  :root {
    --yellow: #f7c41c;
    --paper: #f2f2f2;
    --ink: #1c1c1c;
    --stage: #d9d6d2;
  }
  html, body {
    margin: 0;
    padding: 0;
    width: 1200px;
    height: 900px;
    overflow: hidden;
    background: var(--stage);
    font-family: "Poppins", sans-serif;
  }
  .canvas {
    position: relative;
    width: 1200px;
    height: 900px;
  }
  .card {
    position: absolute;
    width: 620px;
    height: 360px;
    border-radius: 26px;
    overflow: hidden;
    background: var(--paper);
    box-shadow: 0 10px 24px rgba(0,0,0,0.18);
  }

  /* back side */
  .card-back { left: 60px; top: 50px; }
  .card-back .brand-block {
    position: absolute;
    left: 150px;
    top: 0;
    right: 0;
    bottom: 0;
    background: var(--yellow);
  }
  .card-back .wordmark-vertical {
    position: absolute;
    left: 0;
    top: 0;
    width: 360px;
    height: 150px;
    transform-origin: top left;
    transform: rotate(-90deg) translateX(-100%);
    display: flex;
    align-items: center;
    justify-content: center;
    font-weight: 800;
    font-size: 72px;
    line-height: 1;
    color: var(--ink);
    letter-spacing: -1px;
    white-space: nowrap;
  }

  /* front side */
  .card-front { left: 520px; top: 490px; }
  .card-front .brand-panel {
    position: absolute;
    left: 0; top: 0; bottom: 0;
    width: 330px;
    background: var(--yellow);
  }
  .card-front .wordmark {
    position: absolute;
    left: 36px;
    top: 150px;
    font-weight: 800;
    font-size: 50px;
    line-height: 1;
    color: #ffffff;
    letter-spacing: -0.5px;
  }
  .card-front .details {
    position: absolute;
    left: 380px;
    top: 92px;
    color: var(--yellow);
  }
  .person-name {
    margin: 0;
    font-weight: 600;
    font-size: 19px;
    line-height: 1.1;
  }
  .person-role {
    margin: 2px 0 0;
    font-weight: 600;
    font-size: 11px;
  }
  .contact-list {
    list-style: none;
    margin: 46px 0 0;
    padding: 0;
    font-size: 13px;
    font-weight: 400;
  }
  .contact-list li {
    display: flex;
    align-items: center;
    gap: 12px;
    margin-bottom: 14px;
  }
  .contact-icon {
    width: 14px;
    display: inline-flex;
    justify-content: center;
    font-size: 13px;
  }
</style>
</head>
<body>
<main class="canvas">

  <section class="card card-back" aria-label="Card back">
    <div class="brand-block" role="img" aria-label="Brand colour field"></div>
    <div class="wordmark-vertical">SipLoop</div>
  </section>

  <section class="card card-front" aria-label="Card front">
    <div class="brand-panel"></div>
    <div class="wordmark">SipLoop</div>
    <div class="details">
      <p class="person-name">Marco Tessin</p>
      <p class="person-role">Founder</p>
      <ul class="contact-list">
        <li>
          <span class="contact-icon">
            <svg width="9" height="13" viewBox="0 0 9 13" aria-hidden="true">
              <rect x="0.75" y="0.75" width="7.5" height="11.5" rx="1.5" fill="none" stroke="currentColor" stroke-width="1.3"/>
              <line x1="3.3" y1="10" x2="5.7" y2="10" stroke="currentColor" stroke-width="1"/>
            </svg>
          </span>
          001 555 010 200
        </li>
        <li>
          <span class="contact-icon">@</span>
          marco@siploop.example
        </li>
      </ul>
    </div>
  </section>

</main>
</body>
</html>
```